Photo Storage Service - Web Application

This is web design for a simple photo storage service.
There is a web page and on the left side is a list of folders and on the right side there are photo thumbnails. By pressing a photo thumbnail, they will see the full size (it's just a link to a different page).
This project is limited only to ONE page, which is the page with the folders list and the thumbnails. However it contains some features that I will try to list here:
- Name of the service: Teso Vault
- Location of account: http://username.tesovault.example
- Folder list: Show all folders belonging to the user. Because you have to be able to drag photos to a folder, they have to be visible and cannot be hidden behind a menu item etc.
- Thumbnails with photos (in the future also videos)
- Adjusted view with smaller thumbnails and less space for folder list (so it is possible to view a larger quantity of thumbnails)- Select multiple thumbnails with rectangle- Show that a thumbnail is selected (maybe bold border?)
- Simple mobile view, but no emphasis on the mobile view in this design project.
- Drag one or more selected photos to a folder
- Delete one or more selected photos
- Drag a folder to another folder
- Rename folder
- Delete folder
- Create folder
- Show progress when deleting/moving (because it calls for every photo, so if there are 100 photos, it will delete 1 by 1 and it will take about 10 seconds - you could show progress bar or equivalent)
Background information: This is for a photo storage service NOT intended for sharing photos, but intended to indefinitely store photos and for yourself to browse your own photos.
It is a design requirement that it loads extremely fast. So we need to limit as much as possible extra graphics that cannot be done by CSS and other external libraries.
(I know this is ONLY design and nothing to do with CSS or libraries, but I can assess from the design if it might be heavy to load when implemented)
I have attached a crude screenshot of the current design, just for your understanding. It should not match this design and you are not in any way supposed to FIT your design into this same style or structure.
Target Market(s)
Consumers
Number of Pages Required
1 page

```html
<!DOCTYPE html>
<html lang="en">
<head>
<meta charset="utf-8">
<title>Teso Vault</title>
<link href="https://fonts.googleapis.com/css2?family=Nunito+Sans:wght@400;600&display=swap" rel="stylesheet">
<style>
:root{
  --green:#1fb991;
  --ink:#2b2b2f;
  --text:#4a4a4a;
  --muted:#8a8a8a;
  --faint:#b3b3b3;
  --side:#eef0f1;
  --head:#e9eaeb;
  --line:#d4d4d4;
}
*{margin:0;padding:0;box-sizing:border-box}
html,body{width:1200px;height:751px;overflow:hidden;background:#fff;font-family:"Nunito Sans",Arial,sans-serif;color:var(--text)}
.app{position:relative;width:1200px;height:751px;overflow:hidden}
.topbar{position:absolute;left:0;top:0;width:1200px;height:51px;background:#eff0f1}
.brand-area{position:absolute;left:0;top:0;width:266px;height:51px;background:var(--head)}
.brand{position:absolute;left:49px;top:13px;font-size:18px;color:#333;font-weight:400}
.user{position:absolute;left:952px;top:10px;display:flex;align-items:center;gap:7px;font-size:11px;color:#333;white-space:nowrap}
.avatar{width:31px;height:31px;border-radius:50%;background:radial-gradient(circle at 50% 40%,#b08870,#4a3a33)}
.kebab{position:absolute;left:1077px;top:18px}
.sidebar{position:absolute;left:0;top:51px;width:266px;height:700px;background:linear-gradient(180deg,#f3f4f5,#eceeef)}
.sidebar-content{position:absolute;left:0;top:-51px;width:266px;height:751px}
.btn{position:absolute;display:flex;align-items:center;justify-content:center;background:var(--green);color:#fff;border-radius:16px;white-space:nowrap}
.btn-create{left:48px;top:77px;width:115px;height:29px;font-size:13px;gap:6px}
.tool{position:absolute;display:flex;align-items:center;gap:6px;font-size:9px;color:var(--muted);white-space:nowrap}
.tool svg{flex-shrink:0}
.folder{position:absolute;left:64px;font-size:10.5px;color:var(--muted);white-space:nowrap}
.folder.in-drag{color:#333}
.pill{position:absolute;left:48px;width:197px;height:31px;border-radius:16px}
.pill-active{top:192px;background:var(--ink)}
.pill-target{top:534px;background:#c9cacb}
.drag-box{position:absolute;left:46px;top:291px;width:171px;height:212px;background:#d3d4d5;border:1px dashed #555}
.ghost{position:absolute;left:189px;font-size:10.5px;color:#c4c4c4;white-space:nowrap}
.upload{position:absolute;left:286px;top:77px;width:795px;height:157px;border:1px dashed #cfcfcf}
.btn-upload{left:607px;top:150px;width:150px;height:31px;font-size:11px;font-weight:600}
.hint{position:absolute;left:286px;width:795px;text-align:center;font-size:10.5px;color:var(--faint);white-space:nowrap}
.thumb{position:absolute;width:144px;height:138px}
.thumb.selected{outline:1px solid var(--green)}
.play{position:absolute;left:50%;top:50%;width:24px;height:24px;margin:-12px 0 0 -12px}
</style>
</head>
<body>
<div class="app">
  <header class="topbar">
    <div class="brand-area"><div class="brand">Teso Vault</div></div>
    <div class="user"><div class="avatar" role="img" aria-label="User profile photo"></div><span>Daniel Rowe</span></div>
    <svg class="kebab" width="4" height="14" viewBox="0 0 4 14"><circle cx="2" cy="2" r="1.5" fill="#444"/><circle cx="2" cy="7" r="1.5" fill="#444"/><circle cx="2" cy="12" r="1.5" fill="#444"/></svg>
  </header>

  <aside class="sidebar">
    <div class="sidebar-content">
      <div class="btn btn-create"><span style="font-size:16px;line-height:1">+</span>Create Folder</div>
      <div class="tool" style="left:49px;top:125px">
        <svg width="15" height="17" viewBox="0 0 15 17" fill="none" stroke="#1fb991" stroke-width="1.2"><path d="M1 3h13M5 3V1h5v2M2.5 3l1 13h8l1-13"/><path d="M6 6v8M9 6v8"/></svg>
        Delete Folder</div>
      <div class="tool" style="left:49px;top:156px">
        <svg width="19" height="19" viewBox="0 0 19 19" fill="none" stroke="#1fb991" stroke-width="1.2"><rect x="1" y="1" width="10" height="10" stroke-dasharray="2 1.5"/><rect x="7" y="7" width="11" height="11"/><path d="M10 10l5 5M15 11v4h-4"/></svg>
        Drag folder to the destined folder</div>

      <div class="pill pill-active"></div>
      <div class="folder" style="top:200px;color:#fff">Inbox</div>
      <svg style="position:absolute;left:226px;top:201px" width="4" height="13" viewBox="0 0 4 13"><circle cx="2" cy="2" r="1.4" fill="#fff"/><circle cx="2" cy="6.5" r="1.4" fill="#fff"/><circle cx="2" cy="11" r="1.4" fill="#fff"/></svg>

      <div class="folder" style="top:231px">80,s party</div>
      <div class="folder" style="top:262px">A day in Oslo</div>
      <div class="drag-box"></div>
      <div class="folder in-drag" style="top:293px">A Tour of Svendborg</div>
      <div class="folder in-drag" style="top:325px">Alicante 2017</div>
      <div class="folder in-drag" style="top:356px">Bandardan</div>
      <div class="folder in-drag" style="top:387px">Brazil</div>
      <div class="folder in-drag" style="top:418px">Random</div>
      <div class="folder in-drag" style="top:450px">Thailand 1</div>
      <div class="folder in-drag" style="top:481px">Thailand 2</div>
      <div class="pill pill-target"></div>
      <div class="folder" style="top:512px">Usa</div>
      <div class="folder" style="top:543px;color:#555">Thumbnails</div>
      <div class="folder" style="top:574px">Videos/thumbnails</div>

      <div class="ghost" style="top:352px">A Tour of Svendborg</div>
      <div class="ghost" style="top:383px">Alicante 2017</div>
      <div class="ghost" style="top:415px">Bandardan</div>
      <div class="ghost" style="top:446px">Brazil</div>
      <div class="ghost" style="top:477px">Random</div>
      <div class="ghost" style="top:508px;color:#999">Thailand 1</div>
      <div class="ghost" style="top:540px;color:#666">Thailand 2</div>
      <svg style="position:absolute;left:237px;top:550px" width="10" height="14" viewBox="0 0 10 14"><path d="M1 1v11l3-3 2 4 2-1-2-4h4z" fill="#222" stroke="#fff" stroke-width="0.8"/></svg>
    </div>
  </aside>

  <main>
    <section class="upload">
      <svg style="position:absolute;left:366px;top:13px" width="62" height="46" viewBox="0 0 62 46"><path d="M14 45a12 12 0 0 1-1-24 18 18 0 0 1 35-3 13 13 0 0 1 1 27z" fill="#a8a8a8"/><path d="M31 18l-10 11h6v12h8V29h6z" fill="#fff"/></svg>
    </section>
    <div class="btn btn-upload">Choose files to upload</div>
    <div class="hint" style="top:194px">Drag and drop files here to upload.</div>
    <div class="hint" style="top:209px">Files would be automatically saved.</div>

    <div class="tool" style="left:287px;top:277px">
      <svg width="15" height="17" viewBox="0 0 15 17" fill="none" stroke="#1fb991" stroke-width="1.2"><path d="M1 3h13M5 3V1h5v2M2.5 3l1 13h8l1-13"/><path d="M6 6v8M9 6v8"/></svg>
      Delete Select Files</div>
    <div class="tool" style="left:432px;top:276px">
      <svg width="19" height="19" viewBox="0 0 19 19" fill="none" stroke="#1fb991" stroke-width="1.2"><rect x="1" y="1" width="10" height="10" stroke-dasharray="2 1.5"/><rect x="7" y="7" width="11" height="11"/><path d="M10 10l5 5M15 11v4h-4"/></svg>
      Drag files to the destined folder</div>

    <div class="thumb selected" style="left:286px;top:323px;background:linear-gradient(160deg,#8c6a4e,#c75f3a 55%,#d8b8a8)" role="img" aria-label="Video thumbnail: child holding a carved pumpkin">
      <svg class="play" viewBox="0 0 24 24"><circle cx="12" cy="12" r="11" fill="rgba(0,0,0,.25)" stroke="#fff" stroke-width="1.5"/><path d="M9.5 7.5v9l7-4.5z" fill="#fff"/></svg></div>
    <div class="thumb selected" style="left:448px;top:323px;background:linear-gradient(160deg,#6b6a3a,#8b7a48 50%,#4f5330)" role="img" aria-label="Photo: woman lying in the grass"></div>
    <div class="thumb selected" style="left:610px;top:323px;background:linear-gradient(160deg,#c79a6a,#7a5a48 55%,#3e4a6a)" role="img" aria-label="Photo: couple sitting at sunset"></div>
    <div class="thumb" style="left:774px;top:323px;background:linear-gradient(180deg,#f1e4d0,#d9c3a5 55%,#b89d80)" role="img" aria-label="Photo: two girls on a beach"></div>
    <div class="thumb" style="left:936px;top:323px;background:linear-gradient(160deg,#d5d5d5,#8a8a8a 50%,#2c2c2c)" role="img" aria-label="Photo: hands holding a camera"></div>

    <div class="thumb selected" style="left:286px;top:480px;background:linear-gradient(160deg,#c8ccd2,#9a7e64 55%,#5a4638)" role="img" aria-label="Photo: woman in sunglasses outdoors"></div>
    <div class="thumb selected" style="left:448px;top:480px;background:linear-gradient(180deg,#b6c4d8,#6e88a8 45%,#8a4a2a 60%,#4f8fb0)" role="img" aria-label="Photo: rusted shipwreck in the sea"></div>
    <div class="thumb selected" style="left:610px;top:480px;background:linear-gradient(180deg,#c4c4c4,#8d8d8d 55%,#a5a5a5)" role="img" aria-label="Photo: three friends sitting on stairs"></div>
    <div class="thumb" style="left:774px;top:480px;background:linear-gradient(180deg,#6c6a78,#c99a78 50%,#d8cfc8)" role="img" aria-label="Video thumbnail: dancers at sunset">
      <svg class="play" viewBox="0 0 24 24"><circle cx="12" cy="12" r="11" fill="rgba(0,0,0,.25)" stroke="#fff" stroke-width="1.5"/><path d="M9.5 7.5v9l7-4.5z" fill="#fff"/></svg></div>
    <div class="thumb" style="left:936px;top:480px;background:linear-gradient(180deg,#2a2a2a,#d8a888 40%,#c8201e 75%)" role="img" aria-label="Photo: child in a witch costume"></div>
  </main>
</div>
</body>
</html>
```